Create a business promotion flyer to leave in customer mailboxes. We are a bulk petroleum supplier, servicing any industry that requires diesel. Base in griffith NSW, servicing griffith area and surrounds.

Business Name - Terra Petro
Fuel@terrapetro-example.com.au
Marco - 0400 000 001 mtorrisi@terrapetro-example.com.au
Liam - 0400 000 002 lharcourt@terrapetro-example.com.au
Peter - 0400 000 003 pwinslow@terrapetro-example.com.au
Office 02 5550 0100

Bulk Fuel deliveries.
Oils & lubricants
Local Family owned business

```html
<!DOCTYPE html>
<html lang="en">
<head>
<meta charset="utf-8">
<title>Terra Petro – Bulk Fuel Flyer</title>
<link rel="stylesheet" href="https://fonts.googleapis.com/css2?family=Bebas+Neue&family=Poppins:wght@400;500;600;700&display=swap">
<style>
  :root {
    --red: #ed1c24;
    --ink: #231f20;
    --backdrop: #5a5b5d;
    --white: #ffffff;
    --sky-top: #9fb6d8;
    --sky-mid: #dfe6ef;
    --ground: #d8d2cb;
    --ground-low: #e6e0da;
  }
  * { margin: 0; padding: 0; box-sizing: border-box; }
  html, body { width: 1051px; height: 1200px; overflow: hidden; }
  body { background: var(--backdrop); font-family: "Poppins", sans-serif; color: var(--ink); position: relative; }

  .flyer { position: absolute; left: 174px; top: 154px; width: 702px; height: 908px; background: var(--white); overflow: hidden; }

  .hero-photo { position: absolute; left: 0; top: 0; width: 702px; height: 661px;
    background: linear-gradient(180deg, var(--sky-top) 0%, var(--sky-mid) 22%, #b9bec6 38%, #8f959e 48%, #c9c3bc 56%, var(--ground) 75%, var(--ground-low) 100%); }

  .brand { position: absolute; left: 57px; top: 78px; display: flex; align-items: center; gap: 10px; }
  .brand-square { width: 22px; height: 22px; background: var(--red); }
  .brand-name { font-size: 31px; font-weight: 600; color: var(--red); letter-spacing: -0.5px; }

  .service-area { position: absolute; left: 510px; top: 0; width: 166px; height: 202px; background: var(--red);
    color: var(--white); font-size: 17.5px; line-height: 22.5px; text-align: center; padding-top: 52px; font-weight: 400; }
  .service-area strong { font-weight: 700; }

  .headline { position: absolute; left: 58px; top: 345px; font-family: "Bebas Neue", sans-serif; font-size: 87px; line-height: 64.5px; color: var(--ink); letter-spacing: 0.5px; }
  .headline .accent { color: var(--red); }

  .feature-line { position: absolute; left: 430px; top: 370px; width: 1.5px; height: 220px; background: var(--red); }
  .feature-icon { position: absolute; left: 400px; width: 61px; height: 61px; border-radius: 50%; background: var(--red); display: flex; align-items: center; justify-content: center; }
  .feature-icon svg { width: 34px; height: 34px; fill: none; stroke: var(--white); stroke-width: 1.6; stroke-linecap: round; stroke-linejoin: round; }
  .feature { position: absolute; left: 483px; width: 210px; }
  .feature h2 { font-size: 22.5px; line-height: 25px; font-weight: 700; color: var(--ink); letter-spacing: -0.2px; }
  .feature p { font-size: 13.5px; line-height: 16.5px; margin-top: 6px; color: var(--ink); }

  .cta { position: absolute; left: 60px; top: 683px; font-size: 28.5px; line-height: 35px; font-weight: 500; color: var(--ink); }
  .cta .accent { color: var(--red); font-weight: 600; }
  .cta small { display: block; font-size: 15px; line-height: 20px; margin-top: 5px; font-weight: 500; }

  .contact { position: absolute; width: 220px; }
  .contact .row { display: flex; align-items: center; position: relative; }
  .contact .row svg { position: absolute; left: -18px; width: 10px; height: 10px; fill: var(--red); }
  .contact .name { font-size: 17.5px; line-height: 20px; font-weight: 500; }
  .contact .phone { font-size: 17px; line-height: 20px; font-weight: 600; }
  .contact .email { font-size: 9.5px; line-height: 14px; margin-top: 2px; }

  .footer { position: absolute; left: 0; top: 849px; width: 702px; height: 59px; background: var(--red); color: var(--white); display: flex; align-items: center; padding-left: 67px; }
  .footer .lead { font-size: 14.5px; font-weight: 400; }
  .footer .mail-badge { width: 27px; height: 27px; border-radius: 50%; background: var(--ink); margin-left: 11px; display: flex; align-items: center; justify-content: center; }
  .footer .mail-badge svg { width: 13px; height: 10px; }
  .footer .address { font-size: 16px; font-weight: 700; margin-left: 9px; }
</style>
</head>
<body>
  <main class="flyer">
    <div class="hero-photo" role="img" aria-label="Photo of a white fuel road train with two tanker trailers parked in front of a large steel depot shed under a cloudy blue sky, on a concrete yard"></div>

    <div class="brand">
      <span class="brand-square"></span>
      <span class="brand-name">Terra Petro</span>
    </div>

    <div class="service-area">Reliable bulk<br>fuel supply<br>across <strong>Griffith</strong><br>and surrounds</div>

    <h1 class="headline"><span class="accent">Fuel for</span><br>Farming,<br>Transport<br>&amp; Industry</h1>

    <div class="feature-line"></div>

    <div class="feature-icon" style="top:337px">
      <svg viewBox="0 0 34 34"><rect x="8" y="5" width="14" height="25" rx="1"/><rect x="11" y="8" width="8" height="5"/><path d="M15 16c-2 3-3 4-3 5.5a3 3 0 0 0 6 0c0-1.5-1-2.5-3-5.5z"/><path d="M22 12h3l2 3v11a1.5 1.5 0 0 1-3 0v-6h-2"/><path d="M6 30h18"/></svg>
    </div>
    <div class="feature-icon" style="top:449px">
      <svg viewBox="0 0 34 34"><path d="M10 9h15a2 2 0 0 1 2 2v18a1 1 0 0 1-1 1H9a1 1 0 0 1-1-1V14z"/><path d="M10 9L6 5l3-2 4 4"/><path d="M14 17c-2 3-3 4-3 5.5a3 3 0 0 0 6 0c0-1.5-1-2.5-3-5.5z"/><rect x="20" y="16" width="3" height="7" rx="1.5"/><path d="M8 26h19"/></svg>
    </div>
    <div class="feature-icon" style="top:559px">
      <svg viewBox="0 0 34 34"><circle cx="8" cy="12" r="3"/><circle cx="17" cy="10" r="3.3"/><circle cx="26" cy="12" r="3"/><path d="M3 25v-4a4 4 0 0 1 8 0"/><path d="M11 28v-6a6 6 0 0 1 12 0v6"/><path d="M23 21a4 4 0 0 1 8 0v4"/></svg>
    </div>

    <section class="feature" style="top:330px">
      <h2>Bulk Fuel<br>deliveries.</h2>
      <p>Reliable diesel supply<br>for any industry.</p>
    </section>
    <section class="feature" style="top:433px">
      <h2>Oils &amp;<br>lubricants</h2>
      <p>Quality products to keep<br>your equipment<br>performing at its best.</p>
    </section>
    <section class="feature" style="top:553px">
      <h2>Local Family<br>owned business</h2>
      <p>Proudly supporting our<br>local community.</p>
    </section>

    <div class="cta"><span class="accent">Need fuel</span><br>for your<br>operation?<small>Contact Us</small></div>

    <svg width="0" height="0" style="position:absolute">
      <defs>
        <symbol id="i-person" viewBox="0 0 10 10"><circle cx="5" cy="2.7" r="2.3"/><path d="M0.8 10c0-3 1.8-4.6 4.2-4.6S9.2 7 9.2 10z"/></symbol>
        <symbol id="i-phone" viewBox="0 0 10 10"><path d="M3 0.5l1.2 2.4-1 0.9c0.5 1.4 1.2 2.3 2.4 3l1-0.9 2.4 1.3-0.7 2c-4-0.3-7-3.4-7.4-7.5z"/></symbol>
        <symbol id="i-mail" viewBox="0 0 10 10"><path d="M0 2h10v6H0z M0.5 2.5L5 6l4.5-3.5"/></symbol>
        <symbol id="i-office" viewBox="0 0 10 10"><path d="M1 10V3h3V0h5v10zM2 5h1v1H2zM5 2h1v1H5zM7 2h1v1H7zM5 4h1v1H5zM7 4h1v1H7zM5 6h1v1H5zM7 6h1v1H7z"/></symbol>
      </defs>
    </svg>

    <div class="contact" style="left:281px; top:687px">
      <div class="row name"><svg><use href="#i-person"/></svg>Marco</div>
      <div class="row phone"><svg><use href="#i-phone"/></svg>0400 000 001</div>
      <div class="row email"><svg><use href="#i-mail"/></svg>mtorrisi@terrapetro-example.com.au</div>
    </div>
    <div class="contact" style="left:281px; top:773px">
      <div class="row name"><svg><use href="#i-person"/></svg>Peter</div>
      <div class="row phone"><svg><use href="#i-phone"/></svg>0400 000 003</div>
      <div class="row email"><svg><use href="#i-mail"/></svg>pwinslow@terrapetro-example.com.au</div>
    </div>
    <div class="contact" style="left:503px; top:689px">
      <div class="row name"><svg><use href="#i-person"/></svg>Liam</div>
      <div class="row phone"><svg><use href="#i-phone"/></svg>0400 000 002</div>
      <div class="row email"><svg><use href="#i-mail"/></svg>lharcourt@terrapetro-example.com.au</div>
    </div>
    <div class="contact" style="left:503px; top:785px">
      <div class="row name"><svg><use href="#i-office"/></svg>Office</div>
      <div class="row phone"><svg><use href="#i-phone"/></svg>02 5550 0100</div>
    </div>

    <footer class="footer">
      <span class="lead">Have questions? Email us at:</span>
      <span class="mail-badge"><svg viewBox="0 0 13 10"><rect x="0.5" y="0.5" width="12" height="9" fill="#fff"/><path d="M0.5 0.5L6.5 5.5 12.5 0.5" fill="none" stroke="#231f20" stroke-width="1"/></svg></span>
      <span class="address">Fuel@terrapetro-example.com.au</span>
    </footer>
  </main>
</body>
</html>
```